Business Card Design for Portrait photography professional

We are a small company specializing in portrait photography (weddings, family, couples, children, newborn, pregnant, etc.) Occasionally we do business portraits too and do some other type of photography. We need a business card which would fit into the same look and feel as our website theme (lumvika.com - under construction currently).
Our target customer base lies within mid- to upmarket. We want our business cards to convey a feeling of quality, solidness and a bit luxury.
Design should be universal and usable on 85mmx55mm, 90mmx50mm and 90mmx55mm
one extra file (PSD of a website didn't fit into the allowed updoad, therefore has put it into my filecrate: https://www.filecrate-example.net/s/qt7wk2rbvx9dmhe/website%20theme%20PSD.psd)

Target Market(s)

mostly private people, 25-60 years old, mostly well established.

Industry/Entity Type

Portrait Photography

Requirements
Must have
• 2 sided design (print on both sides of the business card).
Must include:
business name, logo, URL (lumvika.no) , employee name, email address, and phone number.
Colorscheme of the website lumvika.no / lumvika.com

```html
<!DOCTYPE html>
<html lang="en">
<head>
<meta charset="utf-8">
<title>Lumvika — Business Card</title>
<link rel="stylesheet" href="https://fonts.googleapis.com/css2?family=Montserrat:wght@300;400&display=swap">
<style>
  :root {
    --backdrop: #d6d4d1;
    --card-black: #121212;
    --card-band: #1d1d1d;
    --band-shadow: #050505;
    --ink-light: #f2f0ec;
    --ink-soft: #d8d6d2;
    --rule: rgba(255, 255, 255, 0.28);
  }
  * { box-sizing: border-box; margin: 0; padding: 0; }
  html, body {
    width: 1200px;
    height: 900px;
    overflow: hidden;
    background: var(--backdrop);
    font-family: "Montserrat", sans-serif;
  }
  .card-sheet {
    position: relative;
    width: 1200px;
    height: 900px;
  }
  .card {
    position: absolute;
    top: 156px;
    width: 380px;
    height: 588px;
    background: var(--card-black);
    box-shadow: 0 14px 30px rgba(0, 0, 0, 0.28);
    overflow: hidden;
    color: var(--ink-light);
  }
  .card--front { left: 160px; }
  .card--back { left: 660px; }

  /* front: vertical band texture */
  .front-texture {
    position: absolute;
    inset: 0;
    background:
      linear-gradient(90deg,
        var(--card-black) 0%,
        var(--card-black) 22%,
        var(--band-shadow) 26%,
        var(--card-band) 30%,
        var(--card-band) 70%,
        var(--band-shadow) 74%,
        var(--card-black) 78%,
        var(--card-black) 100%);
  }
  .brand-mark {
    position: absolute;
    left: 50%;
    top: 50%;
    transform: translate(-50%, -50%);
    display: flex;
    flex-direction: column;
    align-items: center;
    gap: 14px;
  }
  .brand-mark__circle {
    width: 150px;
    height: 150px;
    border-radius: 50%;
    border: 3px solid var(--ink-light);
  }
  .brand-mark__name {
    font-size: 30px;
    font-weight: 400;
    letter-spacing: 0.08em;
    color: var(--ink-light);
  }
  .brand-mark--small { top: 130px; gap: 10px; }
  .brand-mark--small .brand-mark__circle { width: 104px; height: 104px; border-width: 2px; }
  .brand-mark--small .brand-mark__name { font-size: 20px; }

  /* back: contact details */
  .contact {
    position: absolute;
    left: 0;
    right: 0;
    top: 300px;
    text-align: center;
  }
  .contact__name {
    font-size: 24px;
    font-weight: 300;
    letter-spacing: 0.04em;
    padding-bottom: 16px;
  }
  .contact__item {
    font-size: 14px;
    font-weight: 300;
    color: var(--ink-soft);
    letter-spacing: 0.03em;
    padding: 14px 0;
  }
  .contact__rule {
    height: 1px;
    width: 240px;
    margin: 0 auto;
    background: linear-gradient(90deg, transparent, var(--rule), transparent);
  }
</style>
</head>
<body>
  <main class="card-sheet">
    <section class="card card--front" aria-label="Card front">
      <div class="front-texture" role="img" aria-label="Dark woven texture with a central vertical band"></div>
      <div class="brand-mark">
        <div class="brand-mark__circle"></div>
        <span class="brand-mark__name">lumvika.no</span>
      </div>
    </section>

    <section class="card card--back" aria-label="Card back">
      <div class="brand-mark brand-mark--small">
        <div class="brand-mark__circle"></div>
        <span class="brand-mark__name">Lumvika</span>
      </div>
      <div class="contact">
        <p class="contact__name">Mira Solvang</p>
        <div class="contact__rule"></div>
        <p class="contact__item">0370 418 226</p>
        <div class="contact__rule"></div>
        <p class="contact__item">mira@lumvika.com</p>
        <div class="contact__rule"></div>
        <p class="contact__item">lumvika.com</p>
      </div>
    </section>
  </main>
</body>
</html>
```